Brightivo sanitzing wipes: logo, inner foil 6*8cm and consumer carton

we need a clever but simple logo design for a product and integrated look for the packaging (inner foil 6*8 cm and consumer carton). texts are provided for each and some examples of other products and formatting. we would use very simple imagery and color schemes. the main theme is safety, convenience, utility.

for the winning design we will for sure have some changes and adaptations and i would pay additionally for those.

Target Market(s)

American and European retail mass merchants -- wholesale stores, online, retail

Industry/Entity Type

Health And Wellness

Font styles to use
Sans Serif

Requirements
Must have
• Correct formatting of texts in accordance to regulations. Clear communication of texts in an easy to read and understandable formatting. Engaging, but simple design.
Nice to have
• Interesting use of color and contrast. some decent imagery/visual graphics that can make the outter packaging pop on shelf.
Should not have
• odd fonts or formatting. knock-offs of other designs of a similar product in its category, cliché or overused imagery

```html
<!DOCTYPE html>
<html lang="en">
<head>
<meta charset="utf-8">
<title>Brightivo Sanitizing Hand Wipes – Carton</title>
<link href="https://fonts.googleapis.com/css2?family=Montserrat:ital,wght@0,400;0,500;0,600;0,700;0,800;1,600&display=swap" rel="stylesheet">
<style>
  :root {
    --bg: #ffffff;
    --panel-light: #f4f6f5;
    --green: #2dbb7c;
    --green-deep: #1f9d66;
    --green-dark: #16784d;
    --teal: #3ab4df;
    --ink: #2b2f2d;
    --white: #ffffff;
    --edge: #d9dedb;
  }
  * { box-sizing: border-box; margin: 0; padding: 0; }
  html, body { width: 1200px; height: 789px; overflow: hidden; background: var(--bg); }
  body { font-family: "Montserrat", Arial, sans-serif; color: var(--ink); position: relative; }

  .carton-front {
    position: absolute; left: 50px; top: 225px; width: 860px; height: 340px;
    background: linear-gradient(90deg, var(--panel-light) 0%, var(--panel-light) 28%, #bfe6d2 52%, var(--green) 78%, var(--green-deep) 100%);
    border: 1px solid var(--edge);
  }
  .carton-end {
    position: absolute; left: 930px; top: 225px; width: 220px; height: 340px;
    background: linear-gradient(180deg, var(--green) 0%, var(--green-deep) 100%);
    border: 1px solid var(--edge);
    padding: 30px 18px;
  }

  .brand-banner {
    position: absolute; left: 60px; top: 28px; width: 330px; height: 58px;
    background: var(--teal); border-radius: 6px 30px 6px 6px;
    display: flex; align-items: center; padding-left: 26px; gap: 12px;
  }
  .brand-name { color: var(--white); font-weight: 800; font-size: 34px; letter-spacing: 1px; }
  .brand-dot { width: 16px; height: 16px; border-radius: 50%; background: var(--green); }

  .product-line { position: absolute; left: 90px; top: 94px; color: var(--green-dark); }
  .product-line .kind { font-weight: 600; font-size: 15px; letter-spacing: 4px; }
  .product-line .noun { font-weight: 600; font-style: italic; font-size: 22px; margin-left: 12px; color: var(--green-deep); }

  .claim-pill {
    position: absolute; left: 70px; top: 136px; padding: 5px 22px;
    background: var(--green); color: var(--white); border-radius: 14px;
    font-weight: 800; font-size: 13px; letter-spacing: 2px;
  }
  .wipe-size { position: absolute; left: 72px; top: 172px; font-size: 9px; font-weight: 600; letter-spacing: 1px; color: var(--green-dark); }

  .tagline { position: absolute; left: 22px; top: 204px; font-size: 17px; font-weight: 500; color: var(--ink); }

  .uses { position: absolute; left: 22px; top: 240px; display: flex; gap: 22px; list-style: none; }
  .use { display: flex; flex-direction: column; align-items: center; width: 72px; }
  .use svg { width: 48px; height: 48px; }
  .use span { margin-top: 6px; font-size: 10px; font-weight: 600; white-space: nowrap; }
  .use span::before { content: "● "; font-size: 7px; vertical-align: middle; }

  .features { position: absolute; left: 560px; top: 40px; list-style: none; color: var(--white); }
  .features li { font-weight: 700; font-size: 14px; letter-spacing: 3px; margin-bottom: 8px; }
  .features li::before { content: "● "; font-size: 9px; vertical-align: middle; }

  .count-badge {
    position: absolute; left: 700px; top: 150px; width: 110px; height: 58px;
    border: 2px solid var(--white); border-radius: 10px; color: var(--white);
    text-align: center; padding-top: 4px;
  }
  .count-badge strong { display: block; font-size: 26px; font-weight: 800; line-height: 1; }
  .count-badge small { font-size: 9px; font-weight: 600; letter-spacing: 1px; }

  .benefits { list-style: none; color: var(--white); }
  .benefits li { font-size: 11px; font-weight: 500; line-height: 1.4; margin-bottom: 14px; padding-left: 12px; position: relative; }
  .benefits li::before { content: "●"; position: absolute; left: 0; font-size: 8px; top: 2px; }
</style>
</head>
<body>
  <section class="carton-front" aria-label="Carton front panel">
    <div class="brand-banner"><span class="brand-name">Brightivo</span><span class="brand-dot"></span></div>
    <p class="product-line"><span class="kind">SANITIZING HAND</span><span class="noun">wipes</span></p>
    <p class="claim-pill">KILLS 99.99% OF GERMS</p>
    <p class="wipe-size">ONE WIPE: 7.9" x 5.9" – 15cm x 20cm</p>
    <p class="tagline">Brilliantly convenient for cleaning and sanitizing hands and surfaces</p>

    <ul class="uses">
      <li class="use"><svg viewBox="0 0 48 48" fill="none" stroke="#2b2f2d" stroke-width="2"><circle cx="24" cy="24" r="22"/><path d="M13 26l22-8-4 6 4 6-22-4 6-2z" fill="#2b2f2d"/></svg><span>Travel</span></li>
      <li class="use"><svg viewBox="0 0 48 48" fill="none" stroke="#2b2f2d" stroke-width="2"><circle cx="24" cy="24" r="22"/><path d="M12 15h4l4 14h13l3-10H18"/><circle cx="21" cy="33" r="2"/><circle cx="31" cy="33" r="2"/></svg><span>Shopping</span></li>
      <li class="use"><svg viewBox="0 0 48 48" fill="none" stroke="#2b2f2d" stroke-width="2"><circle cx="24" cy="24" r="22"/><path d="M14 24h20M14 18v12M18 16v16M34 18v12M30 16v16"/></svg><span>Gym</span></li>
      <li class="use"><svg viewBox="0 0 48 48" fill="none" stroke="#2b2f2d" stroke-width="2"><circle cx="24" cy="24" r="22"/><path d="M13 34V22l11-7 11 7v12zM21 34v-6h6v6M17 24h3M28 24h3"/></svg><span>School</span></li>
      <li class="use"><svg viewBox="0 0 48 48" fill="none" stroke="#2b2f2d" stroke-width="2"><circle cx="24" cy="24" r="22"/><path d="M13 30h22M16 30v5M32 30v5M19 20h10v8H19z"/></svg><span>Work</span></li>
      <li class="use"><svg viewBox="0 0 48 48" fill="none" stroke="#2b2f2d" stroke-width="2"><circle cx="24" cy="24" r="22"/><path d="M12 24a12 10 0 0 1 24 0zM24 24v11M18 35h12"/></svg><span>Play areas and toys</span></li>
      <li class="use"><svg viewBox="0 0 48 48" fill="none" stroke="#2b2f2d" stroke-width="2"><circle cx="24" cy="24" r="22"/><path d="M12 30v-6l4-7h16l4 7v6zM12 24h24"/><circle cx="17" cy="31" r="2"/><circle cx="31" cy="31" r="2"/></svg><span>Car</span></li>
      <li class="use"><svg viewBox="0 0 48 48" fill="none" stroke="#2b2f2d" stroke-width="2"><circle cx="24" cy="24" r="22"/><circle cx="24" cy="24" r="8"/><path d="M11 14v20M35 14v20"/></svg><span>Before and after meals</span></li>
    </ul>

    <ul class="features">
      <li>70% ALCOHOL</li>
      <li>FRAGRANCE FREE</li>
      <li>PARABEN FREE</li>
      <li>PHTHALATE FREE</li>
    </ul>

    <div class="count-badge"><strong>100</strong><small>DISPOSABLE WIPES</small></div>
  </section>

  <aside class="carton-end" aria-label="Carton end panel">
    <ul class="benefits">
      <li>Kills 99.99% of harmful germs and bacteria</li>
      <li>Cleans hands without soap and water</li>
      <li>Perfectly moist and ready to use every time</li>
      <li>Soft, ultra thick non-woven fabric</li>
      <li>Convenient resealable packaging</li>
      <li>Gently cleans, never sticky</li>
    </ul>
  </aside>
</body>
</html>
```